Modern Innovative Business Card Design

We require a nice, modern, clean business card design, ready for upload to Cardomora. Our company develops online banking software solutions for small financial insitutions. The design should be clean, professional, but yet not "corporate boring". See www.fyrolt.com for an idea of business image and profile. The design should communicate innovation, be modern and fresh, yet look professional and established.

Target Market(s)

Finance industry, bankers, entrepreneurs

Industry/Entity Type

Financial

Contact Information for Business Card

Tobias Wendlerup
CEO

FYROLT BV
Lindenwerf 38
1027 HX Amsterdam
The Netherlands

Phone: +31 20 517 8036
Direct: +31 20 604 1758
Skype: tobias.fyrolt
ceo@fyrolt.com
www.fyrolt.com

Font styles to use
Sans Serif

Requirements
Must have
• Should look clean, modern and professional. File should be ready for upload to cardomora.
Should not have
• Boring standard corporate layout

```html
<!DOCTYPE html>
<html lang="en">
<head>
<meta charset="utf-8">
<title>FYROLT Business Card</title>
<link rel="stylesheet" href="https://fonts.googleapis.com/css2?family=Exo+2:wght@300;400;600&display=swap">
<style>
  :root {
    --backdrop: #e9eaea;
    --card-white: #ffffff;
    --card-grey: #565656;
    --ink-dark: #4a4a4a;
    --ink-light: #e6e6e6;
    --accent-green: #7cc23a;
  }
  * { margin: 0; padding: 0; box-sizing: border-box; }
  html, body {
    width: 1200px;
    height: 1000px;
    overflow: hidden;
    background: var(--backdrop);
  }
  .canvas {
    position: relative;
    width: 1200px;
    height: 1000px;
  }
  .business-card {
    position: absolute;
    left: 350px;
    top: 113px;
    width: 500px;
    height: 774px;
    background: var(--card-white);
    box-shadow: 0 10px 30px rgba(0,0,0,0.12);
    font-family: "Exo 2", "Helvetica Neue", Arial, sans-serif;
    overflow: hidden;
  }
  .accent-shape {
    position: absolute;
    left: 0;
    top: 0;
    width: 500px;
    height: 774px;
  }
  .identity {
    position: absolute;
    left: 0;
    top: 0;
    width: 500px;
    height: 350px;
  }
  .wordmark {
    position: absolute;
    left: 92px;
    top: 212px;
    font-size: 64px;
    font-weight: 400;
    letter-spacing: 4px;
    color: var(--ink-dark);
    line-height: 1;
  }
  .person {
    position: absolute;
    right: 48px;
    top: 286px;
    text-align: right;
    line-height: 1.15;
  }
  .person-name {
    font-size: 22px;
    font-weight: 400;
    letter-spacing: 1px;
    color: var(--ink-dark);
    text-transform: uppercase;
  }
  .person-role {
    font-size: 22px;
    font-weight: 400;
    letter-spacing: 1px;
    color: var(--accent-green);
    text-transform: uppercase;
  }
  .contact-panel {
    position: absolute;
    left: 0;
    top: 350px;
    width: 500px;
    height: 424px;
    background: var(--card-grey);
  }
  .contact-list {
    position: absolute;
    right: 48px;
    top: 44px;
    text-align: right;
    font-size: 21px;
    font-weight: 300;
    line-height: 1.38;
    color: var(--ink-light);
    list-style: none;
  }
  .contact-list .web {
    color: var(--accent-green);
  }
</style>
</head>
<body>
<main class="canvas">
  <article class="business-card">
    <svg class="accent-shape" viewBox="0 0 500 774" aria-hidden="true">
      <polygon points="120,148 240,50 380,50 470,148" fill="var(--accent-green)"/>
    </svg>

    <header class="identity">
      <div class="wordmark">FYROLT</div>
      <div class="person">
        <p class="person-name">Tobias Wendlerup</p>
        <p class="person-role">CEO FYROLT</p>
      </div>
    </header>

    <section class="contact-panel">
      <ul class="contact-list">
        <li>BV Lindenwerf</li>
        <li>38 1027 HX, Amsterdam</li>
        <li>The Netherlands</li>
        <li>Phone: +31 20 517 8036</li>
        <li>Direct: +31 20 604 1758</li>
        <li>Skype: tobias.fyroltceo@fyrolt.com</li>
        <li class="web">www.fyrolt.com</li>
      </ul>
    </section>
  </article>
</main>
</body>
</html>
```